HomePage Design for Lumen Getaways - once-in-a-lifetime experiences for busy working people

Design a homepage for the Lumen Getaways (www.lumengetaways.example) website compatible with further web pages and the design briefing documents attached

LG HomePage Design Brief
We are seeking website HomePage designs incorporating our new Logo and colour scheme, for Lumen Getaways (www.lumengetaways.example) to go with the site functionality and wireframe ideas attached.
The website HomePage design needs to
• Incorporate and be consistent with the LG Logo and its colour scheme attached.
• Express the brand values of being inspirational, high quality, upscale, cultured, aspirational, and contemporary – even somewhat ‘hip’. Probably positioned somewhere between Harlow Pike (Deluxe Travel) and Green Walrus (Hip Travel) – see https://www.harlowpike.example and https://www.greenwalrus.example .
• Be instantly recognisable and different from other travel websites and instantly communicate the nature of the brand proposition and target customer base.
• Appeal to our core 25-55 affluent businesspeople demographic
• Work in the UK, US/Canada and Australia/NZ and ultimately in mainland Europe.
• Use fonts and colours that are easily reproduced online and compatible with nearly all browsers.
• Be part of a responsive website design, that can be used both on Desktops and laptops but also with tablets and mobile ‘phones (hence content not too wide across the page)
• Feature the strapline ‘Lumen Getaways in less than 7 Days’
• Work with the and wireframes and processes shown in the attached presentation – although intended as a guide only these features and processes all need to be incorporated into the HomePage.
• Make full use of high quality images and video to convey our brand proposition and products

Target Market(s)

25-55 affluent businesspeople

Industry/Entity Type

Travel Industry

Number of Pages Required

1 page

Font styles to use
Sans Serif

Colors
0455a3
00a88f

Requirements
Must have
• • Incorporate and be consistent with the LG Logo and its colour scheme attached.
• • Express the brand values of being inspirational, high quality, upscale, cultured, aspirational, and contemporary – even somewhat ‘hip’. Probably positioned somewhere between Harlow Pike (Deluxe Travel) and Green Walrus (Hip Travel) – see https://www.harlowpike.example and https://www.greenwalrus.example .
• • Be instantly recognisable and different from other travel websites and instantly communicate the nature of the brand proposition and target customer base.
• • Appeal to our core 25-55 affluent businesspeople demographic
• • Be part of a responsive website design, that can be used both on Desktops and laptops but also with tablets and mobile ‘phones (hence content not too wide across the page)
• • Feature the strapline ‘Lumen Getaways in less than 7 Days’
• • Work with the and wireframes and processes shown in the attached presentation – although intended as a guide only these features and processes all need to be incorporated into the HomePage.
• • Make full use of high quality images and video to convey our brand proposition and products
• Colours as per Logo not as shown below
Nice to have
• • Work in the UK, US/Canada and Australia/NZ and ultimately in mainland Europe.
Should not have
• Must not be cheap or mass-market, nor excessively "stuffy or luxury-orientated"

```html
<!DOCTYPE html>
<html lang="en">
<head>
<meta charset="utf-8">
<title>Lumen Getaways – Home</title>
<link rel="stylesheet" href="https://fonts.googleapis.com/css2?family=Lato:wght@400;700&display=swap">
<style>
:root{
  --navy:#252f6c;
  --green:#1d6a3a;
  --ink:#2b2b2b;
  --muted:#8a8a8a;
  --line:#dcdcdc;
  --topbar:#f3f3f3;
  --footer:#f1f1f1;
  --white:#ffffff;
}
*{box-sizing:border-box;margin:0;padding:0}
html,body{width:1200px;height:2305px;overflow:hidden}
body{font-family:"Lato",Arial,sans-serif;color:var(--ink);background:var(--white);position:relative}
a{color:inherit;text-decoration:none}

/* top bar */
.topbar{position:absolute;left:0;top:0;width:1200px;height:60px;background:var(--topbar);font-size:13px;color:var(--muted)}
.topbar .item{position:absolute;top:21px;display:flex;align-items:center;gap:8px}
.topbar svg{fill:#b9b9b9}

/* header */
.header{position:absolute;left:0;top:60px;width:1200px;height:121px}
.socials{position:absolute;left:60px;top:50px;display:flex;gap:0}
.socials span{width:14px;height:14px;border-radius:50%;background:#8f8f8f;margin-right:22px;display:block}
.socials span+span{position:relative}
.brand{position:absolute;left:0;width:1200px;top:46px;display:flex;justify-content:center;align-items:center;gap:12px}
.brand .mark{width:22px;height:22px;border-radius:50%;background:var(--green)}
.brand .name{font-size:26px;font-weight:700;color:var(--green);letter-spacing:.5px;text-transform:uppercase}
.login{position:absolute;left:988px;top:37px;width:163px;height:47px;border:1.5px solid var(--green);color:var(--green);font-size:13px;font-weight:700;display:flex;align-items:center;justify-content:center;letter-spacing:.3px}

/* nav */
.nav{position:absolute;left:54px;top:181px;width:1096px;height:50px;display:flex;border:1px solid var(--line);border-bottom:none}
.nav a{flex:auto;display:flex;align-items:center;justify-content:center;font-size:13.5px;font-weight:700;color:#333;border-left:1px solid var(--line);text-transform:uppercase}
.nav a:first-child{border-left:none;color:var(--navy)}

/* hero */
.hero{position:absolute;left:0;top:231px;width:1200px;height:525px;background:linear-gradient(180deg,#7d8fa6 0%,#4f7e9b 28%,#3a8ca5 45%,#2f7f93 60%,#5b8476 78%,#6e6a4f 100%)}
.hero .photo{position:absolute;inset:0;background:radial-gradient(ellipse 40% 55% at 30% 55%,rgba(196,150,90,.75),transparent 70%),radial-gradient(ellipse 25% 40% at 5% 80%,rgba(70,90,50,.7),transparent 70%)}
.hero h1{position:absolute;left:0;width:1200px;top:175px;text-align:center;font-size:43px;font-weight:700;color:var(--white);text-shadow:0 2px 6px rgba(0,0,0,.35)}
.hero p{position:absolute;left:180px;width:840px;top:238px;text-align:center;font-size:19px;line-height:29px;color:var(--white);font-weight:700;text-shadow:0 1px 4px rgba(0,0,0,.4)}
.hero .arrow{position:absolute;top:226px;width:34px;height:34px}

/* booking */
.booking{position:absolute;left:141px;top:678px;width:918px;height:121px;background:var(--white);border:1px solid #e4e4e4;box-shadow:0 2px 6px rgba(0,0,0,.05)}
.booking .label{position:absolute;left:-1px;top:-1px;width:190px;height:122px;background:var(--navy);color:var(--white);font-size:23px;font-weight:700;line-height:29px;padding:34px 0 0 36px}
.select{position:absolute;top:38px;height:43px;border:1px solid #dedede;font-size:13px;color:var(--muted);display:flex;align-items:center;padding-left:26px}
.select .caret{position:absolute;right:0;top:0;width:34px;height:41px;border-left:1px solid #dedede;display:flex;align-items:center;justify-content:center}
.book-now{position:absolute;left:763px;top:38px;width:118px;height:40px;background:var(--green);color:var(--white);font-size:13px;font-weight:700;display:flex;align-items:center;justify-content:center}

/* welcome */
.welcome{position:absolute;left:0;width:1200px;top:896px;display:flex;justify-content:center;align-items:center;gap:12px;font-size:27px}
.welcome .lead{color:#444;letter-spacing:.5px}
.welcome .mark{width:20px;height:20px;border-radius:50%;background:var(--green)}
.welcome .name{color:var(--green);font-weight:700;text-transform:uppercase}

.tile{position:absolute;width:218px}
.tile .img{width:218px;height:217px}
.tile .cap{margin-top:17px;text-align:center;font-size:19px;line-height:23px;color:#333}

/* offers */
.offers-title{position:absolute;left:141px;top:1632px;width:921px;height:26px;display:flex;align-items:center;gap:0}
.offers-title .rule{flex:1;height:1px;background:var(--line)}
.offers-title h2{font-weight:400;font-size:26px;color:#555;width:184px;text-align:center;letter-spacing:.5px}
.offer{position:absolute;top:1718px;width:296px;height:182px}
.offer .img{width:100%;height:100%}
.offer .bar{position:absolute;left:0;bottom:0;width:100%;height:34px;background:rgba(240,240,240,.88);display:flex;align-items:center;padding-left:22px;font-size:14px;color:#444;text-transform:uppercase}
.offer .bar b{font-size:17px;color:#222;text-transform:none;margin-left:auto;margin-right:auto;position:absolute;left:165px}

/* footer */
.footer{position:absolute;left:0;top:2003px;width:1200px;height:249px;background:var(--footer)}
.footer ul{position:absolute;top:71px;list-style:none;font-size:13.5px;line-height:23px;color:#444}
.copybar{position:absolute;left:0;top:2252px;width:1200px;height:53px;background:var(--navy);color:var(--white);font-size:18px}
.copybar .copy{position:absolute;left:56px;top:15px}
.copybar .icons{position:absolute;left:975px;top:12px;display:flex;gap:12px}
.copybar .icons span{width:30px;height:30px;border-radius:50%;background:#3a4585;display:block}
</style>
</head>
<body>

<div class="topbar">
  <div class="item" style="left:62px">
    <svg width="12" height="16" viewBox="0 0 12 16"><path d="M6 0a6 6 0 0 0-6 6c0 4.5 6 10 6 10s6-5.5 6-10a6 6 0 0 0-6-6zm0 8.5A2.5 2.5 0 1 1 6 3.5a2.5 2.5 0 0 1 0 5z"/></svg>
    <span>48 Harbour Row, Brightwater, FL 30000</span>
  </div>
  <div class="item" style="left:807px">
    <svg width="16" height="11" viewBox="0 0 16 11"><path d="M0 0h16v11H0z"/><path d="M0 0l8 6 8-6" fill="none" stroke="#f3f3f3" stroke-width="1.3"/></svg>
    <span>hello@lumengetaways.example</span>
  </div>
  <div class="item" style="left:1036px">
    <svg width="13" height="13" viewBox="0 0 13 13"><path d="M3 0l2 3-1.3 1.6a8 8 0 0 0 4.7 4.7L10 8l3 2-1.5 2.6C6 13 0 7 .4 1.5z"/></svg>
    <span>555-014-2286</span>
  </div>
</div>

<header class="header">
  <div class="socials" aria-label="Social links"><span></span><span></span><span></span><span></span></div>
  <div class="brand"><span class="mark"></span><span class="name">Lumen Getaways</span></div>
  <a class="login" href="#">CLIENT LOGIN</a>
</header>

<nav class="nav">
  <a href="#">Destinations</a>
  <a href="#">Experiences</a>
  <a href="#">Trips by Month</a>
  <a href="#">Tropical Now</a>
  <a href="#">Tailored</a>
  <a href="#">Pioneers Club</a>
  <a href="#">Blogs &amp; Reviews</a>
</nav>

<section class="hero">
  <div class="photo" role="img" aria-label="Coastal village of colourful houses on a cliff above a turquoise harbour with small boats"></div>
  <h1>Lumen Getaways in less than 7 days!</h1>
  <p>Get onboard now for the launch of our brand new online platform offering once-in-a-lifetime experiences for busy people</p>
  <svg class="arrow" style="left:55px" viewBox="0 0 34 34"><circle cx="17" cy="17" r="15.5" fill="none" stroke="#fff" stroke-width="1.5"/><path d="M19 11l-6 6 6 6" fill="none" stroke="#fff" stroke-width="1.5"/></svg>
  <svg class="arrow" style="left:1114px" viewBox="0 0 34 34"><circle cx="17" cy="17" r="15.5" fill="none" stroke="#fff" stroke-width="1.5"/><path d="M15 11l6 6-6 6" fill="none" stroke="#fff" stroke-width="1.5"/></svg>
</section>

<form class="booking">
  <div class="label">Book Your<br>Experience!</div>
  <div class="select" style="left:215px;width:250px">Where do you wanna go ?
    <span class="caret"><svg width="11" height="7" viewBox="0 0 11 7"><path d="M1 1l4.5 4.5L10 1" fill="none" stroke="#999" stroke-width="1.4"/></svg></span></div>
  <div class="select" style="left:490px;width:248px">Why do you wanna go ?
    <span class="caret"><svg width="11" height="7" viewBox="0 0 11 7"><path d="M1 1l4.5 4.5L10 1" fill="none" stroke="#999" stroke-width="1.4"/></svg></span></div>
  <a class="book-now" href="#">BOOK NOW</a>
</form>

<div class="welcome"><span class="lead">WELCOME TO</span><span class="mark"></span><span class="name">Lumen Getaways</span></div>

<div class="tile" style="left:142px;top:977px"><div class="img" role="img" aria-label="Savannah at sunset with mountains and grazing wildlife" style="background:linear-gradient(180deg,#c9a24a 0%,#b07a2c 45%,#6b4a24 70%,#8a6a30 100%)"></div><div class="cap">Wonders of Wildlife</div></div>
<div class="tile" style="left:377px;top:977px"><div class="img" role="img" aria-label="Festival crowd throwing clouds of coloured powder" style="background:linear-gradient(135deg,#e8579a 0%,#9b6ad6 35%,#4fc3a0 65%,#e6c241 100%)"></div><div class="cap">World’s Greatest<br>Festivals</div></div>
<div class="tile" style="left:612px;top:977px"><div class="img" role="img" aria-label="Child splashing in a fountain in a green park" style="background:linear-gradient(160deg,#2f4a1c 0%,#5c7d2a 40%,#1d2a14 100%)"></div><div class="cap">Must Do Activities</div></div>
<div class="tile" style="left:847px;top:977px"><div class="img" role="img" aria-label="Sky lanterns glowing over a dark evening horizon" style="background:linear-gradient(180deg,#1d1a24 0%,#3a2a2a 45%,#b5662a 80%,#e0a050 100%)"></div><div class="cap">Unique Annual Events</div></div>

<div class="tile" style="left:264px;top:1285px"><div class="img" role="img" aria-label="Hidden rocky cave opening with lush greenery" style="background:linear-gradient(160deg,#2a2218 0%,#5a4a30 45%,#7a7a40 75%,#3a3222 100%)"></div><div class="cap">Extraordinary &amp;<br>Secret Places</div></div>
<div class="tile" style="left:500px;top:1285px"><div class="img" role="img" aria-label="Dancer mid-move in a bright studio" style="background:linear-gradient(135deg,#f2f2f2 0%,#dcdcdc 50%,#e0506e 80%,#cfcfcf 100%)"></div><div class="cap">Unforgettable<br>Performances</div></div>
<div class="tile" style="left:735px;top:1285px"><div class="img" role="img" aria-label="Group of hikers with backpacks walking under a blue sky" style="background:linear-gradient(180deg,#9fc7e8 0%,#cfe2f0 45%,#4a4a44 75%,#6b6a4a 100%)"></div><div class="cap">Spectacular Hiking,<br>Climbing &amp; Walking</div></div>

<div class="offers-title"><span class="rule"></span><h2>OFFERS</h2><span class="rule"></span></div>

<div class="offer" style="left:141px"><div class="img" role="img" aria-label="Masked carnival costumes beside gondolas on a lagoon at dusk" style="background:linear-gradient(135deg,#c7342e 0%,#d9a0a0 35%,#a8b4c8 65%,#5d6a80 100%)"></div><div class="bar">Venice Carnival<b>£599pp</b></div></div>
<div class="offer" style="left:456px"><div class="img" role="img" aria-label="Row of stone statues silhouetted against an orange sunset" style="background:linear-gradient(180deg,#c46a18 0%,#e8a030 40%,#6a3410 75%,#2a1608 100%)"></div><div class="bar">Easter Island<b>£2,999pp</b></div></div>
<div class="offer" style="left:767px"><div class="img" role="img" aria-label="Day of the Dead celebration portrait in dark tones" style="background:linear-gradient(135deg,#4a4f3a 0%,#2a2c24 50%,#1a1a18 100%)"></div><div class="bar">Day of the Dead<b>£3,299pp</b></div></div>

<footer class="footer">
  <ul style="left:54px"><li>About Us</li><li>Our Partners</li><li>Newsletter</li><li>FAQS</li></ul>
  <ul style="left:231px"><li>Contact Us</li><li>Booking &amp; Conditions</li><li>Privacy &amp; Cookies</li><li>Terms of Use</li></ul>
  <ul style="left:460px"><li>Financial Protection</li><li>Travel Insurance</li><li>Visas</li><li>Travel Advice</li></ul>
  <ul style="left:695px"><li>Group Bookings</li><li>Tailor-Made &amp; Extra Nights</li><li>Booking Flights</li><li>Careers with LG</li></ul>
  <ul style="left:941px"><li>LG Protecting wildlife &amp; animals,</li><li>and supporting local communities</li><li style="margin-top:9px">Press Room</li></ul>
</footer>

<div class="copybar">
  <span class="copy">© 2017 Lumen Getaways.All Rights Reserved</span>
  <div class="icons" aria-label="Social links"><span></span><span></span><span></span><span></span></div>
</div>

</body>
</html>
```